"Orvane Community Supports" Business Card Design

We are a not for profit disability service that has recently changed its logo and trading name and is in the process of "rebranding".We provide employment, training and accommodation to people with disabilities. We find our new logo fresh and inspiring and would like our new business cards to reflect the same feeling. Our marketing line is "Growth, Opportunity, Empowerment".

Target Market(s)

People with disabilities and their families, carers, support network

Industry/Entity Type

Business

Contact Information for Business Card

NamePositionAddressHead OfficeDirect LineMobileFaxEmailWebsite

Requirements
Must have
• Our logo; space for the above listed information requirements

```html
<!DOCTYPE html>
<html lang="en">
<head>
<meta charset="utf-8">
<title>Orvane Community Supports – Business Card</title>
<link rel="stylesheet" href="https://fonts.googleapis.com/css2?family=Open+Sans:wght@300;400;600;700&display=swap">
<style>
  :root {
    --page-bg: #e9ebee;
    --card-white: #ffffff;
    --brand-blue: #0b4a8f;
    --brand-blue-light: #0d7cc4;
    --brand-blue-dark: #093a78;
    --brand-green: #5e9c2c;
    --logo-blue: #1a4f9c;
    --text-light: #ffffff;
  }
  * { margin: 0; padding: 0; box-sizing: border-box; }
  html, body { width: 1200px; height: 900px; overflow: hidden; }
  body {
    background: var(--page-bg);
    font-family: "Open Sans", Arial, sans-serif;
    display: flex;
    flex-direction: column;
    align-items: center;
    justify-content: center;
    gap: 60px;
  }
  .card {
    position: relative;
    width: 640px;
    height: 366px;
    background: var(--card-white);
    box-shadow: 0 6px 18px rgba(0,0,0,0.15);
    overflow: hidden;
  }
  .card-art { position: absolute; inset: 0; }
  .wordmark {
    display: flex;
    align-items: center;
    gap: 12px;
    color: var(--logo-blue);
    font-weight: 600;
    letter-spacing: 2px;
  }
  .wordmark-dot {
    border-radius: 50%;
    background: var(--brand-green);
  }
  /* back */
  .card-back { display: flex; align-items: center; justify-content: center; }
  .card-back .wordmark { font-size: 64px; }
  .card-back .wordmark-dot { width: 54px; height: 54px; }
  /* front */
  .card-front .wordmark {
    position: absolute;
    right: 50px;
    top: 118px;
    font-size: 48px;
  }
  .card-front .wordmark-dot { width: 40px; height: 40px; }
  .holder {
    position: absolute;
    left: 36px;
    top: 40px;
    color: var(--text-light);
  }
  .holder-name { font-size: 21px; font-weight: 700; }
  .holder-role { font-size: 16px; font-weight: 300; margin-top: 2px; }
  .contact-list {
    position: absolute;
    left: 36px;
    bottom: 28px;
    list-style: none;
    color: var(--text-light);
    font-size: 12.5px;
    line-height: 1.35;
  }
  .contact-list li { display: flex; align-items: flex-start; gap: 7px; }
  .contact-icon { width: 12px; height: 12px; flex: none; margin-top: 3px; }
</style>
</head>
<body>

  <section class="card card-back" aria-label="Card back">
    <div class="wordmark"><span class="wordmark-dot"></span><span>ORV</span></div>
  </section>

  <section class="card card-front" aria-label="Card front">
    <svg class="card-art" viewBox="0 0 640 366" width="640" height="366" aria-hidden="true">
      <defs>
        <radialGradient id="panelGlow" cx="0.45" cy="0.4" r="0.75">
          <stop offset="0" stop-color="#0d7cc4"/>
          <stop offset="1" stop-color="#093a78"/>
        </radialGradient>
      </defs>
      <path d="M0 0 H292 Q382 150 424 366 H0 Z" fill="#5e9c2c"/>
      <path d="M0 0 H281 Q371 150 410 366 H0 Z" fill="#ffffff"/>
      <path d="M0 0 H275 Q364 150 402 366 H0 Z" fill="url(#panelGlow)"/>
    </svg>

    <div class="holder">
      <p class="holder-name">Daniel Reyes</p>
      <p class="holder-role">Owner / C.E.O</p>
    </div>

    <ul class="contact-list">
      <li>
        <svg class="contact-icon" viewBox="0 0 12 12"><circle cx="6" cy="6" r="6" fill="#fff"/><path d="M3 6.5 L6 3.5 L9 6.5 V9 H3 Z" fill="#0b4a8f"/></svg>
        <span>Suite # 410, Elm Bldg,<br>NY 10482</span>
      </li>
      <li>
        <svg class="contact-icon" viewBox="0 0 12 12"><circle cx="6" cy="6" r="6" fill="#fff"/><path d="M4 3 Q3 6 6 9 L8 8 L7 6.5 L6 7 Q5 6 5 5 L5.5 4 Z" fill="#0b4a8f"/></svg>
        <span>555-201-7890</span>
      </li>
      <li>
        <svg class="contact-icon" viewBox="0 0 12 12"><circle cx="6" cy="6" r="6" fill="#fff"/><rect x="4.3" y="2.5" width="3.4" height="7" rx="0.6" fill="#0b4a8f"/></svg>
        <span>555-318-4420</span>
      </li>
      <li>
        <svg class="contact-icon" viewBox="0 0 12 12"><circle cx="6" cy="6" r="6" fill="#fff"/><rect x="3" y="5" width="6" height="3.5" fill="#0b4a8f"/><rect x="4" y="3" width="4" height="2" fill="#0b4a8f"/></svg>
        <span>555-762-0915</span>
      </li>
      <li>
        <svg class="contact-icon" viewBox="0 0 12 12"><circle cx="6" cy="6" r="6" fill="#fff"/><rect x="3" y="4" width="6" height="4" fill="#0b4a8f"/><path d="M3 4 L6 6.3 L9 4" stroke="#fff" stroke-width="0.7" fill="none"/></svg>
        <span>name@orvanesupports.org</span>
      </li>
      <li>
        <svg class="contact-icon" viewBox="0 0 12 12"><circle cx="6" cy="6" r="6" fill="#fff"/><circle cx="6" cy="6" r="3.2" fill="none" stroke="#0b4a8f" stroke-width="0.9"/><path d="M2.8 6 H9.2 M6 2.8 V9.2" stroke="#0b4a8f" stroke-width="0.7"/></svg>
        <span>www.orvanesupports.org</span>
      </li>
    </ul>

    <div class="wordmark"><span class="wordmark-dot"></span><span>ORV</span></div>
  </section>

</body>
</html>
```